Small IT consulting firm needs a new web site

Quillmark Solutions, LLC is a company based out of Arizona with national presence. We work on both national, multinational, and international projects. We are Brindlesoft Partners. Heavy experience and work with Orbitline Control Kit, Vantra, Deskhub 720 . We offer Architecture, Design, Development, and implementation services. We have a specialty in Deskhub 720 migrations and implementations. We also have a specialized practice in Program and Project Management. The design message should foster a feeling of partnership and experience. Attached is my logo.

```html
<!DOCTYPE html>
<html lang="en">
<head>
<meta charset="utf-8">
<title>Quillmark Solutions, LLC</title>
<link href="https://fonts.googleapis.com/css2?family=Montserrat:wght@300;400;700&family=Open+Sans:ital,wght@0,400;0,600;1,400&display=swap" rel="stylesheet">
<style>
:root{
  --red:#c1272d;
  --ink:#2b2b2b;
  --muted:#6f6f6f;
  --header-bg:#f4f4f4;
  --navy:#16243a;
  --navy-deep:#0e1828;
  --dark:#1d1b1a;
  --footer:#2a2a2a;
  --footer-bar:#1e1e1e;
  --footer-text:#9a9a9a;
  --white:#ffffff;
}
*{margin:0;padding:0;box-sizing:border-box}
html,body{width:1200px;height:2894px;overflow:hidden}
body{position:relative;font-family:"Open Sans",Arial,sans-serif;color:var(--ink);background:var(--white)}
.abs{position:absolute}
.site-header{top:0;left:0;width:1200px;height:106px;background:var(--header-bg);border-bottom:3px solid #d8d8d8}
.brand{display:flex;align-items:center;gap:10px}
.brand-square{width:22px;height:22px;background:var(--red)}
.brand-name{font-family:"Montserrat",sans-serif;font-weight:700;color:var(--red);font-size:17px;line-height:1.1}
.header-contact{top:22px;right:100px;font-family:"Montserrat",sans-serif;font-size:12px;color:#555;display:flex;gap:28px}
.header-contact b{color:var(--red);font-weight:400}
.header-contact span{display:flex;align-items:center;gap:7px}
.main-nav{top:68px;left:0;width:1200px;font-family:"Montserrat",sans-serif;font-size:13px;color:#333}
.main-nav a{position:absolute;color:inherit;text-decoration:none;white-space:nowrap}
.hero{top:106px;left:0;width:1200px;height:467px;background:linear-gradient(160deg,#4a3a55 0%,#2a3550 40%,#18233a 100%);text-align:center;color:var(--white)}
.hero h1{position:absolute;top:212px;width:100%;font-family:"Montserrat",sans-serif;font-weight:700;font-size:46px;letter-spacing:1px}
.hero p{position:absolute;top:272px;width:100%;font-family:"Montserrat",sans-serif;font-weight:300;font-size:44px;letter-spacing:1px;text-transform:uppercase}
.about{top:573px;left:0;width:1200px;height:320px}
.about .brand{position:absolute;top:130px;left:200px}
.about-text{top:87px;left:502px;width:560px;font-size:12.5px;line-height:25px;color:var(--muted)}
.partners-band{top:893px;left:0;width:1200px;height:438px;background:linear-gradient(180deg,#1c2c44,var(--navy-deep));color:var(--white)}
.section-title{font-family:"Montserrat",sans-serif;font-weight:700;font-size:26px;text-align:center;width:100%}
.partners-band .section-title{top:104px}
.partners-intro{top:152px;left:150px;width:900px;text-align:center;font-size:15px;line-height:29px}
.partner{top:250px;display:flex;align-items:center;gap:22px}
.partner-icon{width:96px;height:96px;border:2px solid var(--white);border-radius:50%;display:flex;align-items:center;justify-content:center}
.partner h3{font-family:"Montserrat",sans-serif;font-weight:400;font-size:19px;text-transform:uppercase;margin-bottom:6px}
.partner p{font-size:13px}
.services .section-title{top:1404px;color:#2e2e2e}
.service{top:1489px;width:311px}
.service-photo{height:197px}
.service h4{margin-top:22px;font-family:"Montserrat",sans-serif;font-weight:700;font-size:12.5px;line-height:22px;color:#1e2a5a;text-transform:uppercase}
.service p{margin-top:8px;font-size:12.5px;line-height:24px;color:var(--muted)}
.testimonials{top:1902px;left:0;width:1200px;height:428px;background:linear-gradient(135deg,#2b2624,var(--dark) 60%,#0f0e0e);color:var(--white)}
.testimonials .section-title{top:60px}
.quote{top:187px;left:289px;width:410px;font-style:italic;font-size:13px;line-height:26px}
.quote-mark{font-family:Georgia,serif;font-size:42px;line-height:1}
.quote-author{top:303px;left:294px;font-size:13px}
.quote-author b{display:block;font-weight:600;margin-bottom:4px}
.portrait{top:2025px;left:787px;width:186px;height:186px;border-radius:50%;border:4px solid var(--white);background:radial-gradient(circle at 50% 40%,#c9a58e,#5e7a98 70%)}
.client{top:2401px;width:184px;height:102px;border:2px solid #e1e1e1;display:flex;align-items:center;justify-content:center;font-family:"Montserrat",sans-serif;font-weight:700;font-size:18px;color:#444}
.site-footer{top:2562px;left:0;width:1200px;height:274px;background:var(--footer);color:var(--footer-text);font-family:Arial,sans-serif;font-size:11px}
.footer-col{top:52px}
.footer-col h5{font-family:"Montserrat",sans-serif;font-weight:700;font-size:12px;color:var(--white);margin-bottom:14px;text-transform:uppercase}
.footer-col li{list-style:none;height:25px}
.contact-line{display:flex;align-items:center;gap:10px}
.social{display:flex;align-items:center;gap:12px;height:41px}
.social i{width:27px;height:27px;border-radius:50%;background:#4a4a4a;display:block}
.footer-bar{top:2836px;left:0;width:1200px;height:58px;background:var(--footer-bar);color:#8a8a8a;font-size:11px;text-align:center;line-height:58px;font-family:Arial,sans-serif}
</style>
</head>
<body>

<header class="site-header abs">
  <div class="brand abs" style="top:36px;left:100px">
    <span class="brand-square"></span>
    <span class="brand-name">Quillmark<br>Solutions, LLC</span>
  </div>
  <div class="header-contact abs">
    <span><svg width="13" height="13" viewBox="0 0 24 24"><path fill="#777" d="M6.6 10.8a15 15 0 0 0 6.6 6.6l2.2-2.2c.3-.3.7-.4 1-.2 1.1.4 2.3.6 3.6.6.6 0 1 .4 1 1V20c0 .6-.4 1-1 1A17 17 0 0 1 3 4c0-.6.4-1 1-1h3.5c.6 0 1 .4 1 1 0 1.3.2 2.5.6 3.6.1.3 0 .7-.2 1z"/></svg>LOCAL: <b>+1-555-010-2841</b></span>
    <span><svg width="13" height="13" viewBox="0 0 24 24"><path fill="none" stroke="#777" stroke-width="2.5" d="M4 15v-3a8 8 0 0 1 16 0v3"/><rect x="3" y="14" width="4" height="7" rx="1" fill="#777"/><rect x="17" y="14" width="4" height="7" rx="1" fill="#777"/></svg>TOLL FREE: <b>+1-800-555-0193</b></span>
  </div>
  <nav class="main-nav abs">
    <a style="left:498px">HOME</a>
    <a style="left:608px">ABOUT US</a>
    <a style="left:743px">SERVICES</a>
    <a style="left:873px">WHAT WE DO</a>
    <a style="left:1027px">CONTACT US</a>
  </nav>
</header>

<section class="hero abs" role="img" aria-label="Photo of hands typing on a keyboard, tinted dark blue">
  <h1>QUILLMARK SOLUTIONS</h1>
  <p>We are an IT consulting firm</p>
</section>

<section class="about abs">
  <div class="brand">
    <span class="brand-square"></span>
    <span class="brand-name" style="font-size:22px">Quillmark<br>Solutions, LLC</span>
  </div>
  <svg class="abs" style="top:66px;left:412px" width="40" height="186" viewBox="0 0 40 186"><path d="M6 2 C24 2 24 20 24 40 V78 C24 88 28 92 36 93 C28 94 24 98 24 108 V146 C24 166 24 184 6 184" fill="none" stroke="#cfcfcf" stroke-width="3"/></svg>
  <p class="about-text abs">Lorem Ipsum is simply dummy text of the printing and typesetting industry. Lorem Ipsum has been the industry's standard dummy text ever since the 1500s, when an unknown printer took a galley of type and scrambled it to make a type specimen book. It has survived not only five centuries, but also the leap into electronic typesetting, remaining essentially unchanged. It was popularised in the 1960s with the release of Letraset sheets containing Lorem Ipsum passages, and more recently with desktop publishing software like Aldus PageMaker including versions of Lorem Ipsum.</p>
</section>

<section class="partners-band abs" aria-label="We work with">
  <h2 class="section-title abs">WE WORK WITH</h2>
  <p class="partners-intro abs">We offer Architecture, Design, Development, and implementation services. We have a specialty in Deskhub 720 migrations and implementations. We also have a specialized practice in Program and Project Management.</p>
  <div class="partner abs" style="left:100px">
    <span class="partner-icon"><svg width="34" height="34" viewBox="0 0 24 24"><path fill="#fff" d="M11 3h2v9l3-3 1.4 1.4L12 15.8 6.6 10.4 8 9l3 3zM3 17h18v4H3z"/></svg></span>
    <div><h3>Orbitline Control Kit</h3><p>Click here for view more info</p></div>
  </div>
  <div class="partner abs" style="left:453px">
    <span class="partner-icon"><svg width="36" height="36" viewBox="0 0 24 24" fill="#fff"><circle cx="12" cy="7" r="3"/><circle cx="5.5" cy="9" r="2.3"/><circle cx="18.5" cy="9" r="2.3"/><path d="M6 19a6 6 0 0 1 12 0zM1 18a4.5 4.5 0 0 1 6-4 7 7 0 0 0-2 4zM23 18a4.5 4.5 0 0 0-6-4 7 7 0 0 1 2 4z"/></svg></span>
    <div><h3>Vantra</h3><p>Click here for view more info</p></div>
  </div>
  <div class="partner abs" style="left:804px">
    <span class="partner-icon"><svg width="30" height="34" viewBox="0 0 20 24"><rect x="3" y="1" width="14" height="22" fill="none" stroke="#fff" stroke-width="2"/><g fill="#fff"><rect x="6" y="4" width="3" height="3"/><rect x="11" y="4" width="3" height="3"/><rect x="6" y="9" width="3" height="3"/><rect x="11" y="9" width="3" height="3"/><rect x="6" y="14" width="3" height="3"/><rect x="11" y="14" width="3" height="3"/><rect x="8" y="19" width="4" height="4"/></g></svg></span>
    <div><h3>Deskhub 720</h3><p>Click here for view more info</p></div>
  </div>
</section>

<section class="services" aria-label="Services">
  <h2 class="section-title abs">QUILLMARK SOLUTIONS, LLC SERVICES</h2>
  <article class="service abs" style="left:100px">
    <div class="service-photo" role="img" aria-label="Photo of a person with a laptop on a pier under a hot air balloon sky" style="background:linear-gradient(180deg,#9fb3c8,#d8cfc4 60%,#8a7767)"></div>
    <h4>Portfolio, Program and Project Managemnet</h4>
    <p>Lorem Ipsum is simply dummy text of the printing and typesetting industry. Lorem Ipsum has been the industry's standard dummy text ever since the 1500s...</p>
  </article>
  <article class="service abs" style="left:444px">
    <div class="service-photo" role="img" aria-label="Photo of a businessman holding a laptop in front of a city sketch" style="background:linear-gradient(90deg,#d9d9d9,#9c9c9c 60%,#5a5a5a)"></div>
    <h4>Technical Architecture, Design, and Engineering</h4>
    <p>Lorem Ipsum is simply dummy text of the printing and typesetting industry. Lorem Ipsum has been the industry's standard dummy text ever since the 1500s...</p>
  </article>
  <article class="service abs" style="left:789px">
    <div class="service-photo" role="img" aria-label="Photo of a smiling business team" style="background:linear-gradient(180deg,#e8e6e3,#7d7f88 70%,#3b3d45)"></div>
    <h4>Staff Augmentation</h4>
    <p>Lorem Ipsum is simply dummy text of the printing and typesetting industry. Lorem Ipsum has been the industry's standard dummy text ever since the 1500s...</p>
  </article>
</section>

<section class="testimonials abs" aria-label="Testimonials">
  <h2 class="section-title abs">TESTIMONIALS</h2>
  <div class="quote abs">
    <span class="quote-mark abs" style="left:-40px;top:-22px">&ldquo;</span>
    Lorem Ipsum is simply dummy text of the printing and typesetting industry. Lorem Ipsum has been the industry's standard dummy text ever since the 1500s, when an unknown printer took a galley of type and scrambled it to make a type specimen book.
    <span class="quote-mark abs" style="left:403px;top:56px">&rdquo;</span>
  </div>
  <div class="quote-author abs"><b>Marlon Vesty</b>Marketing Executive</div>
</section>
<div class="portrait abs" role="img" aria-label="Portrait photo of the client giving the testimonial"></div>

<section aria-label="Clients">
  <div class="client abs" style="left:100px">Tallyfern</div>
  <div class="client abs" style="left:303px">Orchidpost</div>
  <div class="client abs" style="left:507px">Brennick Larue</div>
  <div class="client abs" style="left:712px">Dozewell Inc</div>
  <div class="client abs" style="left:916px">Halvern</div>
</section>

<footer class="site-footer abs">
  <div class="brand abs" style="top:60px;left:100px">
    <span class="brand-square"></span>
    <span class="brand-name" style="font-size:18px">Quillmark<br>Solutions, LLC</span>
  </div>
  <div class="footer-col abs" style="left:303px">
    <h5>Welcome</h5>
    <ul><li>Home</li><li>About us</li><li>Services</li><li>What we do</li><li>Contact us</li></ul>
  </div>
  <div class="footer-col abs" style="left:475px">
    <h5>Information</h5>
    <ul><li>Terms &amp; Conditions</li><li>Privacy Policy</li><li>Disclaimer</li></ul>
  </div>
  <div class="footer-col abs" style="left:681px">
    <h5>Company Info</h5>
    <ul>
      <li>1180 W Saguaro Lane, Suite 210</li>
      <li>Tempe, AZ 85281-4410</li>
      <li class="contact-line" style="height:30px"><svg width="12" height="12" viewBox="0 0 24 24"><path fill="#9a9a9a" d="M6.6 10.8a15 15 0 0 0 6.6 6.6l2.2-2.2c.3-.3.7-.4 1-.2 1.1.4 2.3.6 3.6.6.6 0 1 .4 1 1V20c0 .6-.4 1-1 1A17 17 0 0 1 3 4c0-.6.4-1 1-1h3.5c.6 0 1 .4 1 1 0 1.3.2 2.5.6 3.6.1.3 0 .7-.2 1z"/></svg>Local: +1-555-010-2841</li>
      <li class="contact-line" style="height:28px"><svg width="12" height="12" viewBox="0 0 24 24"><path fill="none" stroke="#9a9a9a" stroke-width="2.5" d="M4 15v-3a8 8 0 0 1 16 0v3"/><rect x="3" y="14" width="4" height="7" fill="#9a9a9a"/><rect x="17" y="14" width="4" height="7" fill="#9a9a9a"/></svg>Toll Free: +1-800-555-0193</li>
      <li class="contact-line" style="height:29px"><svg width="12" height="12" viewBox="0 0 24 24"><rect x="3" y="9" width="18" height="12" fill="#9a9a9a"/><rect x="7" y="3" width="10" height="6" fill="none" stroke="#9a9a9a" stroke-width="2"/></svg>Fax: +1-555-014-7720</li>
      <li class="contact-line"><svg width="12" height="12" viewBox="0 0 24 24"><rect x="2" y="5" width="20" height="14" fill="#9a9a9a"/><path d="M2 5l10 8 10-8" fill="none" stroke="#2a2a2a" stroke-width="2"/></svg>hello@quillmarksolutions.co</li>
    </ul>
  </div>
  <div class="footer-col abs" style="left:953px">
    <h5>Follow Us</h5>
    <p style="margin-bottom:8px">Connect with our social network</p>
    <div class="social"><i></i>: Friendwall</div>
    <div class="social"><i></i>: Chirpline</div>
    <div class="social"><i></i>: Linkwork</div>
  </div>
</footer>
<div class="footer-bar abs">© 2015. Quillmark. All Rights Reserved.</div>

</body>
</html>
```